International Property Consultancy

Brief Overview:

I need a dynamic and well designed website that is easy to use and understand. It has to be unique and different to generic templates that most websites seem to be these days. PLEASE NO GENERIC TEMPLATES FROM THE INTERNET.

Our business has 10 years experience working on struggling international developments that we then work in-house for to turn around and brings bout success. We stay within a project often for long periods of time until success is achieved. We are unique in our approach and completely different to the standard routes to market for many developments. The site is for developers to see what we have done in regards to previous projects, as such we want to incorporate video into this site with a strong design aesthetic. There will be videos of the past projects we have worked on, which will act as case studies.

I like very simple but punchy websites, that people can navigate and understand very easily. Also a big fan of unique and well thought out design aesthetic.

Initial Site layout thoughts:

1) Homepage:
2) About Us
3) What we've done / Work
This part has the projects we have worked on (France, Portugal, London, Morocco). Each one will have some video content and photo images, but also would be good to have a succinct way to mention what we did and the successes in a clever and punchy way.

4) Contact Us

* This is just a guideline. Would be open to input and creative direction on your own part.

*More details and websites we like can be seen in the brief doc attached.

PLEASE VIEW THE WIREFRAME WORD DOC ATTACHED.

Here there are also some more examples to help:

Here are just a few examples of websites and what I like about them:

- www.velmoro.com (clean, nice geometric design aesthetic, good animation when loading and changing pages well thought out all though also coulee be considered a bit dull and basic after the initial homepage slide)
- https://www.farbridgehub.net (Clean site, quite clinical, lacks video content and doesn't engage greatly).
- https://ruskotile.com (minimal, and like how it mixes the design aesthetic more with video and photo content)

- https://www.amberquillworks.com (like the layout of this and how it displays the projects and work section)

- https://brisk.com (Good use of video content)

- https://loomfield.studio (minimal to the point and mixes design with video and animation etc...)

Here is another couple of cool websites that may help give you some direction: https://halvenquay.com www.brisk.com

Hi there, One of the things I thought would be good on the homepage is to add the logo with a 'digital landscape' before flicking down into a slide with video content of the projects... Just an idea but have posted some pics in the brief. We would get this animated for the site. But if you have better ideas, please do run with them. Thanks,

Target Market(s)

Property developers

Number of Pages Required

4 page

Font styles to use
Other font styles liked:
• Read brief

Requirements
Must have
• Needs to be clean, dynamic and easy to follow on desktop and mobile. We will use it as a kind of portfolio website so will need to embed video of past projects we have worked on.

Read brief in docs.
Nice to have
• Clean
Should not have
• Not be another generic template website.
Not have random property stock photos. (We are not a property agency).

```html
<!DOCTYPE html>
<html lang="en">
<head>
<meta charset="utf-8">
<title>corvalen. — International Property Consultancy</title>
<link rel="stylesheet" href="https://fonts.googleapis.com/css2?family=Jost:wght@400;500&family=Source+Sans+3:wght@500&display=swap">
<style>
  :root {
    --bg-deep: #161b1f;
    --bg-mid: #1f262b;
    --bg-edge: #2a3036;
    --bar-top: #2b2b2b;
    --bar-end: #141414;
    --globe-core: rgba(150, 160, 166, 0.42);
    --globe-edge: rgba(120, 130, 136, 0.18);
    --text: #ffffff;
  }
  * { margin: 0; padding: 0; box-sizing: border-box; }
  html, body {
    width: 1200px;
    height: 676px;
    overflow: hidden;
    background: var(--bg-deep);
  }
  .hero {
    position: relative;
    width: 1200px;
    height: 676px;
    overflow: hidden;
    background:
      radial-gradient(ellipse 900px 520px at 50% 20%, var(--bg-mid), transparent 70%),
      radial-gradient(ellipse 400px 500px at 0% 40%, var(--bg-edge), transparent 70%),
      var(--bg-deep);
    font-family: "Jost", "Futura", sans-serif;
    color: var(--text);
  }
  .top-band {
    position: absolute;
    left: 0; top: 0;
    width: 100%;
    height: 30px;
    background: linear-gradient(90deg, var(--bar-top), var(--bar-end));
  }
  .globe-visual {
    position: absolute;
    left: 194px;
    top: 219px;
    width: 812px;
    height: 812px;
    border-radius: 50%;
    background: radial-gradient(circle at 50% 45%, var(--globe-core) 0%, var(--globe-core) 40%, var(--globe-edge) 75%, transparent 100%);
  }
  .main-nav {
    position: absolute;
    top: 34px;
    right: 43px;
    display: flex;
    gap: 31px;
  }
  .main-nav a {
    position: relative;
    color: var(--text);
    text-decoration: none;
    font-size: 13px;
    font-weight: 400;
    letter-spacing: 1.6px;
  }
  .main-nav a.is-active::after {
    content: "";
    position: absolute;
    left: 50%;
    bottom: -6px;
    width: 4px;
    height: 4px;
    margin-left: -2px;
    border-radius: 50%;
    background: var(--text);
  }
  .brand-name {
    position: absolute;
    left: 0;
    width: 100%;
    top: 188px;
    text-align: center;
    font-size: 168px;
    font-weight: 500;
    letter-spacing: -3px;
    line-height: 1;
    color: var(--text);
  }
  .scroll-cue {
    position: absolute;
    left: 0;
    width: 100%;
    top: 586px;
    display: flex;
    flex-direction: column;
    align-items: center;
    gap: 9px;
  }
  .scroll-cue span {
    font-family: "Source Sans 3", "Helvetica", sans-serif;
    font-size: 10.5px;
    font-weight: 500;
    letter-spacing: 0.4px;
  }
</style>
</head>
<body>
  <main class="hero">
    <div class="top-band"></div>
    <div class="globe-visual" role="img" aria-label="Glowing digital globe made of connected points, a digital landscape"></div>

    <nav class="main-nav">
      <a href="#" class="is-active">HOME</a>
      <a href="#">ABOUT</a>
      <a href="#">WORKS</a>
      <a href="#">CONTACT</a>
    </nav>

    <h1 class="brand-name">corvalen.</h1>

    <div class="scroll-cue">
      <svg width="18" height="28" viewBox="0 0 18 28" aria-hidden="true">
        <rect x="0.75" y="0.75" width="16.5" height="26.5" rx="8.25" fill="none" stroke="#ffffff" stroke-width="1.2"/>
        <circle cx="9" cy="9" r="2.2" fill="#ffffff"/>
      </svg>
      <span>Scroll down</span>
    </div>
  </main>
</body>
</html>
```